Business card design needed

My company does everything from wiring up your exisiting entertainment system, to installing a complete new system for you. We can mount your plasma on the wall, install an aerial point for you, setup some surround sound in your outdoor area or install a new cinema room in your house. Any Audio or Visual requirements you may have we can provide these for you. If you want to have a party to remember at your place or just some chilled sounds by the pool, we can give you just the right size system.

Industry/Entity Type

Entertainment

Contact Information for Business Card

The Tune Crew
Colin Pemberton
e| colin@thetunecrew.com.au
w| www.thetunecrew.com.au
m| 0412 576 208

Requirements
Must have
• The logo that i have uploaded is just a starter...something similar to this but not exact or any new suggestions you have would be great too. Colour choice we are pretty easy on we did think Red and Yellow but happy to take advice, something that stands out from the rest i guess.

```html
<!DOCTYPE html>
<html lang="en">
<head>
<meta charset="utf-8">
<title>The Tune Crew – Business Card</title>
<link rel="stylesheet" href="https://fonts.googleapis.com/css2?family=PT+Sans+Narrow:wght@400;700&display=swap">
<style>
  :root {
    --page: #ffffff;
    --brand-yellow: #fddb4d;
    --brand-black: #000000;
    --ink: #111111;
  }
  html, body {
    margin: 0;
    padding: 0;
    width: 1000px;
    height: 1200px;
    overflow: hidden;
    background: var(--page);
  }
  .canvas {
    position: relative;
    width: 1000px;
    height: 1200px;
    font-family: "PT Sans Narrow", "Arial Narrow", sans-serif;
  }
  .card {
    position: absolute;
    left: 59px;
    top: 376px;
    width: 878px;
    height: 507px;
    display: flex;
  }
  .card__brand {
    position: relative;
    width: 563px;
    height: 100%;
    background: var(--brand-yellow);
    color: var(--ink);
  }
  .card__contact {
    position: relative;
    flex: 1;
    height: 100%;
    background: var(--brand-black);
    color: var(--brand-yellow);
  }
  .brand-name {
    position: absolute;
    left: 0;
    right: 0;
    top: 200px;
    margin: 0;
    text-align: center;
    font-weight: 400;
    font-size: 84px;
    line-height: 1;
    letter-spacing: 1px;
  }
  .website {
    position: absolute;
    left: 0;
    right: 0;
    top: 428px;
    margin: 0;
    text-align: center;
    font-size: 33px;
    line-height: 1;
  }
  .person-name {
    position: absolute;
    left: 0;
    right: 0;
    top: 41px;
    margin: 0;
    text-align: center;
    font-weight: 700;
    font-size: 33px;
    line-height: 1;
  }
  .contact-list {
    position: absolute;
    left: 36px;
    top: 389px;
    margin: 0;
    padding: 0;
    list-style: none;
    font-size: 24px;
    line-height: 46px;
  }
  .contact-list__label {
    display: inline-block;
    width: 20px;
    text-align: right;
    margin-right: 4px;
  }
</style>
</head>
<body>
<div class="canvas">
  <section class="card">
    <div class="card__brand">
      <h1 class="brand-name">The Tune Crew</h1>
      <p class="website">www.thetunecrew.com.au</p>
    </div>
    <div class="card__contact">
      <h2 class="person-name">Colin Pemberton</h2>
      <ul class="contact-list">
        <li><span class="contact-list__label">e</span>| colin@thetunecrew.com.au</li>
        <li><span class="contact-list__label">m</span>| 0412 576 208</li>
      </ul>
    </div>
  </section>
</div>
</body>
</html>
```